Bref créative
Business Cards + Stationary for IT Company
Datavertiza
Simple
Rodrigo Baltierra
Presidente & CEO
Oriente 275 No. 512-408
Industrial Montoro
04710, Tlalmivara, D.F.
rb@datavertiza.com
www.datavertiza.com
Please include the Zentrik Logos on the back or front depending of design and distribution
Company logo with commercial name
Company logo with no commercial name
Back card Zentrik partner logo
Back card Certified specialist
Enterprise Premier Partner
This image shall be in the front in a smaller size than company logo.

```html
<!DOCTYPE html>
<html lang="es">
<head>
<meta charset="utf-8">
<title>Datavertiza — Tarjetas de presentación</title>
<link rel="stylesheet" href="https://fonts.googleapis.com/css2?family=Questrial&family=Arimo:wght@400;700&display=swap">
<style>
  :root {
    --stage: #4a4744;
    --card-white: #ffffff;
    --brand-blue: #1a8fd6;
    --brand-blue-light: #3fb0ea;
    --brand-blue-dark: #0f74b8;
    --ink: #4b4b4b;
    --ink-soft: #7a7a7a;
    --strip-light: #f2f2f2;
    --strip-mid: #d6d6d6;
    --on-blue: #ffffff;
  }
  * { box-sizing: border-box; margin: 0; padding: 0; }
  html, body { width: 1200px; height: 718px; overflow: hidden; }
  body {
    background: var(--stage);
    position: relative;
    font-family: "Questrial", "Century Gothic", sans-serif;
    color: var(--ink);
  }
  .card {
    position: absolute;
    border-radius: 14px;
    overflow: hidden;
    box-shadow: 0 4px 14px rgba(0,0,0,.35);
  }

  /* Front card */
  .card-front { left: 34px; top: 34px; width: 562px; height: 643px; background: var(--card-white); }
  .front-logo {
    position: absolute; left: 80px; top: 80px;
    display: flex; align-items: center; gap: 18px;
  }
  .logo-square { width: 62px; height: 62px; background: var(--brand-blue); }
  .logo-name { font-size: 50px; color: var(--ink); line-height: 1; }
  .name-strip {
    position: absolute; left: 0; top: 232px; width: 100%; height: 44px;
    background: linear-gradient(90deg, var(--strip-light), var(--strip-mid));
    display: flex; align-items: center; padding-left: 60px;
    font-family: "Arimo", Arial, sans-serif; font-size: 20px;
  }
  .person-name { font-weight: 700; color: var(--ink); }
  .divider { width: 1px; height: 22px; background: var(--ink-soft); margin: 0 20px; }
  .person-role { color: var(--ink-soft); font-size: 17px; }
  .contact-panel {
    position: absolute; left: 0; top: 276px; width: 100%; bottom: 0;
    background: linear-gradient(180deg, var(--brand-blue-light), var(--brand-blue));
    color: var(--on-blue);
    font-family: "Arimo", Arial, sans-serif; font-size: 16px; line-height: 1.45;
  }
  .address { position: absolute; left: 0; width: 270px; top: 44px; text-align: right; }
  .contact-list { position: absolute; left: 300px; top: 24px; list-style: none; }
  .contact-list li { display: flex; align-items: center; gap: 8px; height: 24px; }
  .contact-list svg { width: 16px; height: 16px; flex: none; }

  /* Back cards */
  .card-back { left: 619px; width: 547px; height: 316px; }
  .card-back-blue { top: 34px; background: linear-gradient(135deg, var(--brand-blue-light), var(--brand-blue-dark)); color: var(--on-blue); }
  .card-back-white { top: 365px; background: var(--card-white); }
  .back-logo {
    position: absolute; left: 0; right: 0; top: 88px;
    display: flex; flex-direction: column; align-items: center; gap: 14px;
  }
  .back-logo .logo-square { width: 86px; height: 86px; }
  .card-back-blue .logo-square { background: var(--on-blue); }
  .back-logo .logo-name { font-size: 46px; }
  .card-back-blue .logo-name { color: var(--on-blue); }
  .partner-name {
    position: absolute; right: 30px; bottom: 26px;
    font-size: 30px; line-height: 1;
  }
  .card-back-blue .partner-name { color: var(--on-blue); }
  .card-back-white .partner-name { color: var(--ink-soft); }
</style>
</head>
<body>

<section class="card card-front" aria-label="Frente de tarjeta">
  <div class="front-logo">
    <span class="logo-square"></span>
    <span class="logo-name">datavertiza</span>
  </div>
  <div class="name-strip">
    <span class="person-name">Rodrigo Baltierra</span>
    <span class="divider"></span>
    <span class="person-role">Presidente &amp; CEO</span>
  </div>
  <div class="contact-panel">
    <p class="address">Oriente 275 No. 512-408<br>Industrial Montoro<br>04710, Tlalmivara, D.F.</p>
    <ul class="contact-list">
      <li>
        <svg viewBox="0 0 16 16"><path d="M3 2h3l1 3-2 1c1 2 2 3 4 4l1-2 3 1v3c-6 0-10-4-10-10z" fill="none" stroke="currentColor" stroke-width="1.4"/></svg>
        +52 55 4318-2750
      </li>
      <li>
        <svg viewBox="0 0 16 16"><rect x="4" y="1.5" width="8" height="13" rx="1.5" fill="none" stroke="currentColor" stroke-width="1.4"/><circle cx="8" cy="12" r="0.9" fill="currentColor"/></svg>
        +521 55 6091-4482
      </li>
      <li>
        <svg viewBox="0 0 16 16"><rect x="1.5" y="3.5" width="13" height="9" fill="none" stroke="currentColor" stroke-width="1.4"/><path d="M1.5 3.5 8 9l6.5-5.5" fill="none" stroke="currentColor" stroke-width="1.4"/></svg>
        rb@datavertiza.com
      </li>
      <li>
        <svg viewBox="0 0 16 16"><circle cx="8" cy="8" r="6.3" fill="none" stroke="currentColor" stroke-width="1.4"/><path d="M1.7 8h12.6M8 1.7c-3 3.5-3 9 0 12.6M8 1.7c3 3.5 3 9 0 12.6" fill="none" stroke="currentColor" stroke-width="1.1"/></svg>
        www.datavertiza.com
      </li>
    </ul>
  </div>
</section>

<section class="card card-back card-back-blue" aria-label="Reverso azul">
  <div class="back-logo">
    <span class="logo-square"></span>
    <span class="logo-name">datavertiza</span>
  </div>
  <span class="partner-name">Zentrik</span>
</section>

<section class="card card-back card-back-white" aria-label="Reverso blanco">
  <div class="back-logo">
    <span class="logo-square"></span>
    <span class="logo-name">datavertiza</span>
  </div>
  <span class="partner-name">Zentrik</span>
</section>

</body>
</html>
```